Elegant, Modern, Sleek Professional - FULL PAGE AD

(8.5” w x 11”w trim size)
We are looking for a sleek, modern, elegant professional full page ad that utilizes our logo and also incorporates the following information:
BRAVA Description:
BRAVA Adjusters, proudly headquartered in New York State, is the premier independent (daily and catastrophe) adjusting firm and third party administrator operating throughout the Northeastern United States, Kansas and Florida. BRAVA offers comprehensive and fully customized loss adjustment programs that are tailored to the specific needs of our clients and their policyholders. Our core-value commitment to traditional integrity based customer service models, unparalleled communication and utilization of InsurTech empowers BRAVA to be the industry leader in our service territories. Additionally, our team has extensive experience with highly complex first and third party claim matters and is a leader in Complex Claim/Large Loss Adjustment, Property Appraiser and Umpire services throughout the entire United States and U.S. Virgin Islands.
Contact:
Desmond R. Halloway
Chief Operating Officer
BRAVA Adjusters | Birch Lantern Loss Bureau, Inc.
418 Meadowlark Lane
PO Box 962
Clifton Park, NY 12079
(800) 555-0187, Ext. 2641
dhalloway@bravaclaimsdesk.example

```html
<!DOCTYPE html>
<html lang="en">
<head>
<meta charset="utf-8">
<title>BRAVA Adjusters – Full Page Ad</title>
<link href="https://fonts.googleapis.com/css2?family=Montserrat:wght@400;600;700;800&family=Open+Sans:wght@400;600&display=swap" rel="stylesheet">
<style>
  :root {
    --orange: #f28a1e;
    --orange-deep: #e0700c;
    --purple: #4b2a8c;
    --ink: #3a3a3a;
    --grey-bg: #eceef1;
    --white: #ffffff;
  }
  html, body { margin: 0; padding: 0; overflow: hidden; background: #2b2b2b; }
  .ad-page {
    position: relative; width: 900px; height: 1200px; overflow: hidden;
    background: var(--white); font-family: "Open Sans", Arial, sans-serif; color: var(--ink);
  }
  .skyline-backdrop {
    position: absolute; left: 0; top: 0; width: 900px; height: 600px;
    background: linear-gradient(180deg, #f6f7f9 0%, var(--grey-bg) 55%, #dde0e5 100%);
  }
  .header-shapes { position: absolute; left: 0; top: 0; }
  .brand-name {
    position: absolute; right: 50px; top: 70px; width: 440px; text-align: center;
    font-family: "Montserrat", Arial, sans-serif; font-weight: 800; font-size: 88px;
    letter-spacing: 6px; line-height: 1; color: var(--orange); margin: 0;
  }
  .portrait {
    position: absolute; left: 55px; top: 185px; width: 340px; height: 390px;
    background: linear-gradient(180deg, #d9dce2 0%, #b7bcc6 60%, #8e95a3 100%);
  }
  .company-description {
    position: absolute; left: 430px; top: 210px; width: 420px;
    font-size: 14px; line-height: 1.75; color: #444; margin: 0;
  }
  .swoosh { position: absolute; left: 0; top: 520px; }
  .service-photos { position: absolute; left: 0; top: 560px; width: 900px; height: 200px; }
  .service-photo {
    position: absolute; top: 10px; width: 170px; height: 170px; border-radius: 50%;
    border: 8px solid var(--purple); box-sizing: border-box;
  }
  .service-photo.one { left: 185px; background: radial-gradient(circle at 40% 40%, #b9c8e0, #4d5f85); }
  .service-photo.two { left: 365px; background: radial-gradient(circle at 50% 45%, #ffd27a, #c2561a); }
  .service-photo.three { left: 545px; background: radial-gradient(circle at 50% 50%, #ffb14a, #7a2c12); }
  .contact { position: absolute; left: 0; top: 790px; width: 900px; text-align: center; }
  .contact-name {
    font-family: "Montserrat", Arial, sans-serif; font-weight: 800; font-size: 40px;
    letter-spacing: 2px; color: var(--orange); margin: 0 0 10px;
  }
  .contact-line {
    font-family: "Montserrat", Arial, sans-serif; font-size: 18px; line-height: 1.5;
    color: var(--ink); margin: 0;
  }
  .contact-line.phone { font-weight: 700; font-size: 20px; }
  .contact-line.title { font-weight: 600; }
  .footer-band { position: absolute; left: 0; bottom: 0; }
  .footer-url {
    position: absolute; left: 0; bottom: 26px; width: 900px; text-align: center;
    font-family: "Montserrat", Arial, sans-serif; font-weight: 700; font-size: 20px;
    letter-spacing: 3px; color: var(--white);
  }
</style>
</head>
<body>
<main class="ad-page">
  <div class="skyline-backdrop" role="img" aria-label="Faint city skyline in pale grey"></div>

  <svg class="header-shapes" width="900" height="600" viewBox="0 0 900 600" aria-hidden="true">
    <path d="M0 0 H260 L90 600 H0 Z" fill="var(--orange)"/>
    <path d="M260 0 H290 L120 600 H90 Z" fill="var(--orange-deep)" opacity="0.6"/>
  </svg>

  <p class="brand-name">BRAVA</p>

  <div class="portrait" role="img" aria-label="Portrait photo of the chief operating officer in a light shirt"></div>

  <p class="company-description">BRAVA Adjusters is an independent adjusting firm and third party administrator handling daily and catastrophe claims across a wide regional territory. We build complete, custom loss adjustment programs shaped around the needs of each client and the policyholders they serve. Our commitment to honest, personal service, clear and timely communication and smart use of modern claims technology keeps our team ahead in every market we cover. Our adjusters also bring deep experience with complex first and third party matters, and we lead in large loss adjustment, property appraisal and umpire services nationwide, supported by seasoned staff who answer every call with care and resolve each file with speed and fairness.</p>

  <svg class="swoosh" width="900" height="140" viewBox="0 0 900 140" aria-hidden="true">
    <path d="M0 120 C250 40 600 30 900 60 V90 C600 60 260 80 0 140 Z" fill="var(--purple)"/>
    <path d="M0 140 C260 80 600 60 900 90 V100 C600 75 270 95 0 140 Z" fill="var(--orange)"/>
  </svg>

  <div class="service-photos">
    <div class="service-photo one" role="img" aria-label="Photo of a flooded neighborhood"></div>
    <div class="service-photo two" role="img" aria-label="Photo of a building fire at night"></div>
    <div class="service-photo three" role="img" aria-label="Photo of a house engulfed in flames"></div>
  </div>

  <section class="contact">
    <h1 class="contact-name">DESMOND R. HALLOWAY</h1>
    <p class="contact-line phone">(800) 555-0187, Ext. 2641</p>
    <p class="contact-line">dhalloway@bravaclaimsdesk.example</p>
    <p class="contact-line title">Chief Operating Officer</p>
    <p class="contact-line">BRAVA Adjusters | Birch Lantern Loss Bureau, Inc.</p>
    <p class="contact-line">418 Meadowlark Lane | PO Box 962 | Harrowfield, Lakeshire 12079</p>
  </section>

  <svg class="footer-band" width="900" height="110" viewBox="0 0 900 110" aria-hidden="true">
    <path d="M0 30 C300 10 600 10 900 25 V110 H0 Z" fill="var(--purple)"/>
    <path d="M0 45 C300 25 600 25 900 40 V110 H0 Z" fill="var(--orange)"/>
  </svg>
  <div class="footer-url">www.bravaclaimsdesk.example</div>
</main>
</body>
</html>
```